Business Card Design Project - Photographer

Photography business needs a logo. I would like to see creative licence on options on 1 & 2 sided. I really like the concept of a fully / partially frosted design. I have already used ArtHive for my Logo, so I am looking for the same level of assistance with this project.

If you have any questions please let me know

Cheers Dorian

Reason: Unsure why but the duration was not even a day long

Industry/Entity Type

Business

Requirements
Must have
• These are my contact details
Name: Dorian Welcombe
Mobile: 0438 612 907
email: dorian@brightlensstudio.com.au
Website: www.brightlensstudio.com.au
Nice to have
• Facebook: https://www.facebook.com/BrightLensStudioOz

```html
<!DOCTYPE html>
<html lang="en">
<head>
<meta charset="utf-8">
<title>BrightLens Studio – Business Card</title>
<link rel="stylesheet" href="https://fonts.googleapis.com/css2?family=Questrial&display=swap">
<style>
  :root {
    --page-bg: #e6e7e8;
    --frost-top: #c4c7ca;
    --frost-bottom: #aeb2b6;
    --frost-edge: #d6d8da;
    --band: #f2f2f2;
    --ink: #2a2a2a;
    --ink-soft: #3c3c3c;
    --accent: #c4232b;
  }
  * { box-sizing: border-box; margin: 0; padding: 0; }
  html, body {
    width: 1200px;
    height: 1000px;
    overflow: hidden;
    background: var(--page-bg);
    font-family: "Questrial", "Century Gothic", sans-serif;
  }
  .canvas {
    position: relative;
    width: 1200px;
    height: 1000px;
  }
  .card {
    position: absolute;
    left: 150px;
    top: 216px;
    width: 900px;
    height: 568px;
    border-radius: 34px;
    background: linear-gradient(170deg, var(--frost-top), var(--frost-bottom));
    border: 2px solid var(--frost-edge);
    box-shadow: 0 18px 40px rgba(0, 0, 0, 0.18);
    overflow: hidden;
  }
  .card__band {
    position: absolute;
    left: 0;
    right: 0;
    top: 92px;
    height: 262px;
    background: var(--band);
    display: flex;
    align-items: center;
  }
  .brand {
    display: flex;
    align-items: center;
    gap: 16px;
    margin-left: 72px;
    width: 360px;
  }
  .brand__mark {
    width: 34px;
    height: 34px;
    background: var(--accent);
    flex: none;
  }
  .brand__name {
    font-size: 38px;
    color: var(--ink);
    letter-spacing: 0.5px;
    white-space: nowrap;
  }
  .contact {
    margin-left: 40px;
    color: var(--ink-soft);
  }
  .contact__name {
    font-size: 34px;
    color: var(--ink);
    margin-bottom: 22px;
  }
  .contact__line {
    font-size: 22px;
    line-height: 1.45;
  }
</style>
</head>
<body>
  <main class="canvas">
    <section class="card" aria-label="Frosted business card">
      <div class="card__band">
        <div class="brand">
          <span class="brand__mark" aria-hidden="true"></span>
          <span class="brand__name">BrightLens Studio</span>
        </div>
        <div class="contact">
          <p class="contact__name">Dorian Welcombe</p>
          <p class="contact__line">dorian@brightlensstudio.com.au</p>
          <p class="contact__line">www.brightlensstudio.com.au</p>
          <p class="contact__line">p: 0438 612 907</p>
        </div>
      </div>
    </section>
  </main>
</body>
</html>
```